My Professional Resume/CV Design

Hi Pixel Harbor experts, I need a professional resume/CV design for using my carrier hiring activities. I have a draft and this draft is 2 types.
1) Traditional IT Major Company Senior(Manager Level) to Director level application (File: Tanabe_Emiko_Res_EN2023AprA)
>Application example companies: Velmora, Drakt, Quindle, Brightmarsh, HoltenWare, Fenwick Ridge, Zentravix, Morivon, Quorexa, Plinth, dZop, Kelvarna etc
>This should not be fancy. Please make format with traditional/gentle/standard but also need to appear unique point such as icons, borderlines etc
2) Cutting-Edge (Web 3.0/metaverse/NFT/Crypto) Start-up or Young (Less 5 year's history) Company Director and C-Levels position application (Tanabe_Emiko_Res_EN2023Apr_typeC)
>Application Example Companies: Tessaluk Studios, Vorlexa, Zintaro.example, Wovenpath, Lumbrook, FernPocket, Thaxel, Kipa/Dult/Snov, Morvik, QUESTAN, wordLYM etc
>This resume format should be something "edge" "advanced" "future" and "high-tech", so need to your high sense of design technics.
Both drafts is without a profile picture, but I need to put in my portfolio picture (Just attached one is my 2018's, you can trim and edit as well)
For the document format, please send me to WORD and PAGES both. and total MAX 2 page in all contents please (No more 3 pages)
Target Market(s)
Traditional Major Tech Company's VP/Directors or/and Latest Web 3.0 StartUp C-Levels (CEO/CTO/CSO/COO etc)
Industry/Entity Type
Technology
Font styles to use
Other font styles liked:
- Choose 3 a)Century Gothic b) Avenir c)Graphik d)Kohinoor e)Optima f)Platino
Look and feel
Each slider illustrates characteristics of the customer's brand and the style your logo design should communicate.

```html
<!DOCTYPE html>
<html lang="en">
<head>
<meta charset="utf-8">
<title>Emiko Tanabe — Resume</title>
<link href="https://fonts.googleapis.com/css2?family=Montserrat:wght@500;600;700&family=Nunito+Sans:wght@400;600;700&display=swap" rel="stylesheet">
<style>
  :root{
    --purple-deep:#6e1f6a;
    --purple:#8a2d86;
    --purple-mid:#a04a9c;
    --lilac:#c98ac4;
    --lilac-soft:#e6c6e3;
    --ink:#2b2b2b;
    --ink-soft:#444;
    --sidebar:#f3f3f4;
    --canvas:#e8e8eb;
    --white:#fff;
  }
  *{box-sizing:border-box;margin:0;padding:0}
  html,body{width:1050px;height:1200px;overflow:hidden}
  body{background:var(--canvas);font-family:"Nunito Sans",Arial,sans-serif;color:var(--ink);position:relative}
  .page{position:absolute;top:243px;width:505px;height:714px;background:var(--white);overflow:hidden;box-shadow:0 2px 10px rgba(0,0,0,.18)}
  .page--one{left:15px}
  .page--two{left:530px}
  .footer-band{position:absolute;left:0;right:0;bottom:0;height:10px}
  .footer-band svg{display:block;width:100%;height:100%}

  /* page one */
  .corner-block{position:absolute;left:20px;top:0;width:47px;height:70px;background:linear-gradient(160deg,var(--purple-mid),var(--purple-deep))}
  .corner-block::after{content:"";position:absolute;left:0;right:0;top:42px;height:1px;background:rgba(255,255,255,.5)}
  .portrait{position:absolute;left:299px;top:37px;width:127px;height:157px;border-radius:10px;background:linear-gradient(160deg,#3a3a3e,#1c1c20 60%,#4b5566)}
  .name{position:absolute;left:20px;top:92px;font-family:Montserrat,Arial,sans-serif;font-weight:700;font-size:28px;letter-spacing:.5px;color:var(--purple-deep);white-space:nowrap}
  .name span{color:var(--purple)}
  .location{position:absolute;left:21px;top:127px;font-family:Montserrat,Arial,sans-serif;font-weight:600;font-size:12.5px;letter-spacing:.4px;color:var(--lilac)}
  .contact{position:absolute;left:24px;top:148px;display:flex;gap:26px;font-family:Montserrat,Arial,sans-serif;font-weight:600;font-size:8.4px;color:var(--purple-deep)}
  .contact-item{display:flex;align-items:center;gap:6px}
  .contact-item svg{width:8px;height:8px;fill:none;stroke:var(--purple);stroke-width:1.4}
  .rule{position:absolute;height:1.5px;background:var(--purple)}
  .rule--a{left:20px;top:159px;width:275px}
  .rule--b{left:432px;top:159px;width:35px}

  .sidebar{position:absolute;left:0;top:176px;width:172px;bottom:10px;background:var(--sidebar)}
  .section-title{font-family:Montserrat,Arial,sans-serif;font-weight:600;font-size:11px;letter-spacing:.3px;color:var(--purple)}
  .sidebar .section-title{position:absolute;left:22px;top:8px}
  .competencies{position:absolute;left:22px;top:29px;list-style:none}
  .competencies li{font-size:7.6px;font-weight:600;color:var(--ink);height:18.6px;display:flex;align-items:center;gap:5px}
  .competencies li::before{content:"";width:2.6px;height:2.6px;border-radius:50%;background:var(--ink)}
  .education{position:absolute;left:0;top:372px;width:172px;height:106px;background:linear-gradient(160deg,var(--purple-mid),var(--purple-deep));color:var(--white);text-align:center;padding-top:16px}
  .education h3{font-family:Montserrat,Arial,sans-serif;font-weight:600;font-size:11px;letter-spacing:.3px;margin-bottom:8px}
  .education p{font-size:7.4px;line-height:1.4}
  .education p + p{margin-top:10px}

  .main{position:absolute;left:183px;top:208px;width:311px}
  .role-headline{font-family:Montserrat,Arial,sans-serif;font-weight:600;font-size:8.6px;color:var(--purple);line-height:1.3;text-align:justify;text-align-last:justify}
  .role-headline .last{display:block;text-align-last:left}
  .tagline{margin-top:7px;font-size:7.3px;font-weight:700;line-height:1.3;text-align:justify}
  .summary{margin-top:7px;font-size:6.3px;line-height:1.32;color:var(--ink-soft);text-align:justify}
  .core{margin-top:8px;font-size:7.3px;font-weight:700;line-height:1.3;text-align:justify}
  .experience-band{position:absolute;left:170px;top:445px;width:335px;height:49px;background:linear-gradient(90deg,var(--purple-mid),var(--purple-deep));color:var(--white);text-align:center;padding-top:7px}
  .experience-band h2{font-family:Montserrat,Arial,sans-serif;font-weight:600;font-size:10.5px;letter-spacing:.3px}
  .experience-band p{font-size:8px;margin-top:4px;letter-spacing:.2px}
  .main--lower{top:503px}

  .job-title{font-family:Montserrat,Arial,sans-serif;font-weight:600;font-size:7.3px;color:var(--purple);line-height:1.3}
  .job-body{font-size:6.3px;line-height:1.32;color:var(--ink-soft);text-align:justify;margin-top:5px}
  .job-body p + p{margin-top:5px}
  .job-body p.bullet{text-indent:6px}

  /* page two */
  .highlights{position:absolute;left:0;top:0;width:162px;height:459px;background:linear-gradient(165deg,var(--purple-mid),var(--purple-deep) 70%);color:var(--white);padding:16px 10px 0 10px}
  .highlights h2{font-family:Montserrat,Arial,sans-serif;font-weight:600;font-size:11.5px;line-height:1.25;letter-spacing:.3px;margin-bottom:12px}
  .highlights p{font-size:6.3px;line-height:1.34;text-indent:6px}
  .highlights p + p{margin-top:9px}
  .lower-left{position:absolute;left:9px;top:472px;width:145px}
  .lower-left .job-body{color:var(--ink-soft)}
  .right-col{position:absolute;left:174px;top:20px;width:320px}
  .right-col .job + .job{margin-top:6px}
</style>
</head>
<body>

<!-- Page one -->
<section class="page page--one">
  <div class="corner-block"></div>
  <div class="portrait" role="img" aria-label="Portrait photo of Emiko Tanabe in a light blazer against a dark backdrop"></div>
  <h1 class="name">EMIKO <span>TANABE</span></h1>
  <div class="location">TAI HANG CRESCENT, HONG KONG</div>
  <div class="contact">
    <span class="contact-item">
      <svg viewBox="0 0 10 10"><path d="M2 1 L4 1 L4.6 3.2 L3.4 4 Q4.4 6 6 6.6 L6.8 5.4 L9 6 L9 8 Q5 9.4 1 3 Z"/></svg>
      +852 5550 1874
    </span>
    <span class="contact-item">
      <svg viewBox="0 0 10 10"><rect x="1" y="2" width="8" height="6"/><path d="M1 2 L5 5.5 L9 2"/></svg>
      etanabe.cv@mailbox.example
    </span>
  </div>
  <div class="rule rule--a"></div>
  <div class="rule rule--b"></div>

  <aside class="sidebar">
    <h2 class="section-title">CORE COMPETENCIES</h2>
    <ul class="competencies">
      <li>Global Operations Management</li>
      <li>Strategic Partnerships</li>
      <li>Process Improvement Champion</li>
      <li>Strategic Planning &amp; Execution</li>
      <li>Cryptocurrency | B2B &amp; B2C</li>
      <li>Research &amp; Development</li>
      <li>Key Account Management</li>
      <li>Business Restructuring</li>
      <li>Team Leadership / Management</li>
      <li>P &amp; L / Revenue Growth</li>
      <li>Budget Management</li>
      <li>Sales B2B + B2G</li>
      <li>Staff Training / Retention</li>
      <li>Business Administration</li>
      <li>Supply Chain &amp; Logistics</li>
      <li>Vendor / Financial Management</li>
      <li>Negotiations &amp; Agreements</li>
      <li>Records &amp; Documentation</li>
    </ul>
    <div class="education">
      <h3>EDUCATION</h3>
      <p>Bachelor's Degree in Economics<br>/ Philosophy</p>
      <p>Kasumigaoka University, Japan</p>
    </div>
  </aside>

  <div class="main">
    <p class="role-headline">Business Development | Cutting Edge Technology | Partner <span class="last">Channel Sales</span></p>
    <p class="tagline">Wide-range Propose Ability / Strategic Planning &amp; Execution / Be As A Professional Middleman Between Japan/apac/global</p>
    <p class="summary">My value and career will only increase in a diverse and multinational work environment. High-impact growth-oriented professional demonstrating a strong grasp of current marketing tools and strategies aligned with cutting-edge technology with an interest in the transformation of society/era events within the industry and cyber security with an entrepreneurial sprit. Strategically collaborate with external vendors and internal business partners; manages various commercial platforms, systems, domains, and channels to ensure scale marketing and lead development capabilities in line with business growth plans that deliver high-quality results. Participate in supply chain strategy development, developing implementation plans, and methods of dealing with business. Display strong analytical ability to evaluate end-to-end customer experience across multiple channels and customer touchpoints. Highly creative with experience in identifying target audiences and devising digital campaigns while valuing traditional methods that engage, inform, and motivate while staying abreast of industry trends.</p>
    <p class="core">“Cutting-Edge Technologies” “Business Development” and “Japan/ APAC Channel Sales” are my main core.</p>
  </div>

  <div class="experience-band">
    <h2>PROFESSIONAL EXPERIENCE</h2>
    <p>(&amp; *Reason for Leaving write end of each carrier paragraph)</p>
  </div>

  <div class="main main--lower">
    <p class="job-title">Inside Renewals Sales | Northgate Shieldworks | Hong Kong<br>Jul 2022 - Present</p>
    <div class="job-body">
      <p>First visa-sponsored employee since the establishment of the APAC Hong Kong company (2017 and in total over 100+). Promotion to Territory Manager (Inside New Sales) is factored in. The agreement to start with renewal sales was to be able to build relationships with existing partners and to set the stage for the new position. Due to internal circumstances, there is no budgetary visibility for an Inside Sales Manager for the Japan Territory. Job hunting activity while still employed for reasons of wanting to advance own careers external, as prospects for promotion within the company are very low expectations by company reasons.</p>
      <p class="bullet">• Distributor and Reseller (Partner) Management: Before I join, the partner side was the low position for any of the partner's sales, like quotation production due to only focused PO. I focusing what end users face on the problems and pain and shared with proper partners. A result, they never ask me for a quotation (they now can quote themself) and they proposed me to new sales plans and strategies. I just concentrated to do what my partner want and relationship development.</p>
      <p class="bullet">• Co-work with Territory Regional Team remotely: Mainly Japan Sales, SEs, CS, Technical Support</p>
      <p class="bullet">• Enhancing mutual synergies with other regional teams: Corporate team works with especially APAC another region team ( India/SEA/ANZ/China total 4 regions) and US and EMEA as well.</p>
    </div>
  </div>

  <div class="footer-band">
    <svg viewBox="0 0 505 10" preserveAspectRatio="none">
      <rect width="505" height="10" fill="#8a2d86"/>
      <polygon points="290,10 300,0 330,0 320,10" fill="#e6c6e3"/>
      <polygon points="325,10 335,0 505,0 505,10" fill="#a04a9c"/>
    </svg>
  </div>
</section>

<!-- Page two -->
<section class="page page--two">
  <aside class="highlights">
    <h2>HIGHLIGHTS OF<br>QUALIFICATION</h2>
    <p>• As Bridge to the gap of Japanese business culture faced by many non - Japanese companies. The Japanese market is potentially huge and digital transformation is lagging behind, there is a lot of opportunities to take a market share. Most of their weakness is “Culture Difference” rather than “language”, I am a native Japanese, fluent English Speaker, and as a business developer is familiar with business practices in Japan/other than Japan, I have confidence fulfill the role of mutual understanding</p>
    <p>• Expert in conducting marketing research and analyzing data strategically to identify brand / product value proposition, prospect customers, markets, and major competitors while utilizing PM software (visualization with 5W1H details)</p>
    <p>• Understands target audiences and competition dynamics with insights from the various premise sources while leading integrated digital and offline marketing campaigns from concept to execution, on time and within scope and budget.</p>
    <p>• Serve as supply chain interfaces for all major projects, with clear knowledge in project progress, logistics and distribution development consideration with each customer journey, and implementation and execution from upper to lower streams.</p>
    <p>• Conceptualize and develop brand / product marketing plans and campaigns for companies and individual business lines, including planning, liaison, coordination and execution.</p>
  </aside>

  <div class="lower-left">
    <p class="job-title">Business Development Manager | Quillon Global | Hong Kong | Apr2019 –Mar 2020</p>
    <div class="job-body">
      <p>cutting-edge science such as human-type robots; creating program/production budgets and completed all interactions with the research institute on behalf of the TV station and also planned the 12 episodes of the first episode</p>
      <p class="bullet">• Spearhead Japan and China's incorporation in the investigation and introduction of cutting-edge technology to which enhanced operational productivity and efficiency for Calvera partners.</p>
      <p class="bullet">• In the Ministry of IT Calvera, presented Humanoid robotics usage for TV presenter collaborated with Calvera TV directors. *Having received notification that funding from the Calveran government has been frozen for six months due to the pandemic</p>
    </div>
  </div>

  <div class="right-col">
    <div class="job">
      <p class="job-title">Business Development Manager | Corvane HK Limited | Hong Kong Apr 2021- Apr 2022</p>
      <div class="job-body">
        <p>Join from GM's direct invitation because he wants to survive the pandemic crisis, this is an IT reseller business provider in Hong Kong, China, SEA, and Japan market. Upon long-term mainly prospective business development and strategy, then proposed better to downsizing and restructuring inclusive me, I suggest leaving this company and GM accepted (Still best relationships).</p>
        <p class="bullet">• <b>As a Management Strategy and Business Development</b> Proposed various restructuring options including M&amp;A, collaboration with the competitors, high demanded IT solutions, Web Marketing campaigns especially for sleeping existing customers reclamation (Company running 30 years)</p>
        <p class="bullet">• <b>Daily Operation as a CRM/Sales/Key Accounting</b> “One Stop Solutions” expert and salesperson as a 100+ client's information systems department. Providing 6 core IT-related services to located at both Hong Kong and China mainland B2B/ B2G based customers with respect and according to their requirements, corporate culture, size, nature, and policies.</p>
        <p class="bullet">• <b>Involvement with client VC advisory service.</b> Seeking potential cutting-edge technology or software-related start-ups. Or performing technical due diligence and making judgments on the product of companies presented by the client-side for operating the best portfolio.</p>
      </div>
    </div>
    <div class="job">
      <p class="job-title">Advisor of Business Development| Pellucid High-Tech (Hong Kong) Limited | Hong Kong &nbsp;&nbsp; May 2020 – Mar 2021</p>
      <div class="job-body">
        <p>I joined the company after contacting the person responsible for developing a medical digital device to prevent the COVID-19 pandemic and presenting the business to the company to achieve commercial success.</p>
        <p class="bullet">• Business development of organic disinfectant water creation devices A new generation of organic disinfectant devices was launched at a part of medical places in Japan. Producing disinfectant water only with tap water and replacing alcohol. In order to bring the organization from being a group of developers to commercial professionals, various operations were required. Since a basic framework generates, the necessary tasks are identified, responsibilities were allocated to a proper person in charge, a business plan was drawn up with a rough timeline and scenario. Due to a change in policy, which focuses on commercial success in Japan before the Asian and global markets, I am no longer heavy responsibility for the project and am now involved just as a non-accountable advisor.</p>
        <p class="bullet">• Business Development of new flying mobility start-up Development of a business plan for the production and development of the new Flying Mobility, the brainchild of the company's president. I've left this and hand over to the proper person such as the financial department for fundraising. *Low expectations that the fundraising would be executed quickly, and a headhunting request from the GM of Corvane HK Limited</p>
      </div>
    </div>
    <div class="job">
      <p class="job-title">Head of Division | Stackwell Tech Limited (Brindlemoor Group (Holdings) Ltd. | Hong Kong &nbsp;| &nbsp;May 2016 – Mar 2019</p>
      <div class="job-body">
        <p>Started work as one of the key players of Fin-Tech industry, Management, and head of operations of a platform for digital assets. When I first joined the company, it was just me as a junior manager + the CEO means actual 1 staff number, by 2018, the FinTech division had grown to 15 people in the Hong Kong office, over 100 people in total including BPO partners in Japan, the Philippines, Netherlands, etc. In this two-year period, I have achieved a total of 4 promotions and achieved my working carrier breakthroughs.</p>
        <p class="bullet">• Outperformed corporate expectations in leading and supervising digital asset white label exchange operations by improving systems that cannot be managed before I join and implementing process improvement initiatives and manuals.</p>
        <p class="bullet">• Adept in managing multiple projects, achieving stable operational exchange, contributing to end-user increase from 1.5K to 5K.</p>
        <p class="bullet">• Nominated Taiwan subsidiary head of a startup, between May to Oct 2017, Spearhead global business operations while overseeing the Taiwan subsidiary business expansion to Taiwanese partner b2b clients and handover to the local manager.</p>
      </div>
    </div>
    <div class="job">
      <p class="job-title">Project Manager | PT. Lanterra Bali | Tokyo &amp; Denpasar| &nbsp;&nbsp; 2014 – 2015</p>
      <div class="job-body" style="margin-top:2px">
        <p class="bullet">• Possessed a stellar review in the strategic planning of corporate projects with B2B institutions at Bali of Indonesia Microfinance and Property Corporate. *Relocate to Hong Kong by my personal reason at the time late of 2015</p>
      </div>
    </div>
    <div class="job">
      <p class="job-title">Chief Operation Officer | Meridao Agency | Tokyo| &nbsp;&nbsp; 2010 – 2014</p>
      <div class="job-body" style="margin-top:2px">
        <p class="bullet">• Structured and pioneered the process of running the Tokyo branch of a Singaporean restaurant by connecting with the F&amp;B company. Demonstrated strength in PR including the English Media to increase brand awareness and clientele growth. *The business cessation requirements of the JV Agreement are met. (Reason cannot be given due to confidentiality, but I can answer orally.)</p>
      </div>
    </div>
  </div>

  <div class="footer-band">
    <svg viewBox="0 0 505 10" preserveAspectRatio="none">
      <rect width="505" height="10" fill="#8a2d86"/>
      <polygon points="0,10 10,0 130,0 120,10" fill="#a04a9c"/>
      <polygon points="125,10 135,0 160,0 150,10" fill="#e6c6e3"/>
    </svg>
  </div>
</section>

</body>
</html>
```